White Rum brand needs bottle label

Looking for a label that will stand out on a shelf and feel like an instant classic. Corvane is a premium Caribbean blended white rum that was crafted as an escape from day-to-day stress and is all about making each day feel as though it's a vacation day. It was named after two local beaches and surf breaks both of which are party towns. I'd like the label to feel modern, sleek, and casual, while still feeling very slightly upscale and have a few subtle hints of it's tropical origin. Corvane should look suitable to drink in variety of situations such as a casual drink at the beach or a pool, a cocktail after a long day of work, or a night out at a bar or club. Please incorporate the logo somewhere in the label, whether that's just the mermaid or the entire design I'll leave that up to the designer. Whatever it is, it should have a look that is scalable and feels appropriate to consume in many settings while remembering it's Carribean and beach roots.

Target Market(s)

The target market is fairly broad. Target consumers are between 21-55, leaning slightly more towards the masculine crowd, full-time workers that enjoy drinking regularly.

Font styles to use
Serif
Sans Serif

Requirements
Must have
• Must have at least the mermaid part of the logo incorporated within the label.
Nice to have
• I'd like a bottle with a synthetic cork, that has a strap sealer over the top and a bottle shaped similar to Valdoro Tequila. Colors are designer's choice. Subtle floral or tropical notes (not too much) mixed into a fairly sleek and modern design.

```html
<!DOCTYPE html>
<html lang="en">
<head>
<meta charset="utf-8">
<title>Corvane White Rum – Label</title>
<link rel="stylesheet" href="https://fonts.googleapis.com/css2?family=Playfair+Display:wght@700&family=Montserrat:wght@600;700&display=swap">
<style>
  :root {
    --backdrop: #f2f2f0;
    --label-slate: #4d5c69;
    --label-slate-deep: #43515d;
    --gold: #c9a96a;
    --gold-light: #e2c88f;
    --ink: #2e3a45;
  }
  html, body {
    margin: 0;
    width: 1200px;
    height: 2276px;
    overflow: hidden;
    background: var(--backdrop);
  }
  .canvas {
    position: relative;
    width: 1200px;
    height: 2276px;
  }
  .label {
    position: absolute;
    left: 150px;
    top: 598px;
    width: 900px;
    height: 1080px;
  }
  .label-body { fill: var(--label-slate); }
  .label-frame { fill: none; stroke: var(--gold); stroke-width: 4; }
  .arc-line {
    font-family: "Montserrat", sans-serif;
    font-weight: 700;
    font-size: 30px;
    letter-spacing: 6px;
    fill: var(--gold-light);
  }
  .est-side {
    font-family: "Montserrat", sans-serif;
    font-weight: 600;
    font-size: 22px;
    letter-spacing: 3px;
    fill: var(--gold-light);
  }
  .brand-name {
    font-family: "Playfair Display", serif;
    font-weight: 700;
    font-size: 118px;
    fill: var(--gold);
  }
  .product-name {
    font-family: "Playfair Display", serif;
    font-weight: 700;
    font-size: 150px;
    fill: var(--gold);
  }
  .ribbon-text {
    font-family: "Montserrat", sans-serif;
    font-weight: 700;
    font-size: 28px;
    letter-spacing: 3px;
    fill: var(--ink);
  }
  .established {
    font-family: "Montserrat", sans-serif;
    font-weight: 600;
    font-size: 26px;
    letter-spacing: 5px;
    fill: var(--gold-light);
  }
  .ribbon { fill: var(--gold); }
  .ribbon-fold { fill: #a88a4f; }
  .divider { stroke: var(--gold); stroke-width: 4; }
</style>
</head>
<body>
<main class="canvas">
  <svg class="label" viewBox="0 0 900 1080" xmlns="http://www.w3.org/2000/svg">
    <defs>
      <path id="crest-arc" d="M150,270 Q450,0 750,270"/>
    </defs>

    <path class="label-body"
          d="M90,230 Q450,-50 810,230 L810,590 L900,590 L900,1020 L840,1080 L60,1080 L0,1020 L0,590 L90,590 Z"/>
    <path class="label-frame"
          d="M112,240 Q450,-20 788,240 L788,612 L878,612 L878,1010 L830,1058 L70,1058 L22,1010 L22,612 L112,612 Z"/>

    <text class="arc-line" text-anchor="middle">
      <textPath href="#crest-arc" startOffset="50%">PREMIUM CARIBBEAN BLENDED</textPath>
    </text>
    <text class="est-side" x="215" y="380" text-anchor="middle">EST.</text>
    <text class="est-side" x="685" y="380" text-anchor="middle">2021</text>

    <text class="brand-name" x="450" y="470" text-anchor="middle">Corvane</text>

    <line class="divider" x1="60" y1="650" x2="840" y2="650"/>

    <text class="product-name" x="450" y="800" text-anchor="middle">White Rum</text>

    <g class="premium-ribbon">
      <polygon class="ribbon-fold" points="190,850 230,850 230,920 190,920 210,885"/>
      <polygon class="ribbon-fold" points="710,850 670,850 670,920 710,920 690,885"/>
      <rect class="ribbon" x="220" y="838" width="460" height="72"/>
      <text class="ribbon-text" x="450" y="884" text-anchor="middle">PREMIUM CARIBBEAN BLENDED</text>
    </g>

    <text class="established" x="450" y="975" text-anchor="middle">ESTD 2021</text>
  </svg>
</main>
</body>
</html>
```